VeroTide Powerpoint design

We've recently redesigned our logos and would like a single presentation format that we can easily interchange the logos attached into. The presentation will be used for general company sales information. The group is called VeroTide and has 2 companies, k7gridworks and Quiet Harbor. We're an IT services company who specialises in Broadband and general network services.

Target Market(s)

Professional

```html
<!DOCTYPE html>
<html lang="en">
<head>
<meta charset="utf-8">
<title>VeroTide – Presentation Template</title>
<link href="https://fonts.googleapis.com/css2?family=Lato:wght@400;700;900&display=swap" rel="stylesheet">
<style>
:root{
  --canvas:#e7e8ea;
  --slide:#f2f2f2;
  --navy:#13224d;
  --blue:#1f3a8a;
  --ink:#2b2f38;
  --muted:#7a7f8a;
  --rule:#1f3a8a;
  --card:#f7f7f7;
  --shadow:0 3px 8px rgba(20,30,60,.12);
}
*{box-sizing:border-box;margin:0;padding:0}
html,body{width:720px;height:1200px;overflow:hidden}
body{background:var(--canvas);font-family:"Lato",Arial,sans-serif;color:var(--ink);position:relative}
.slide{position:absolute;width:283px;height:157px;background:var(--slide);box-shadow:0 6px 16px rgba(20,30,60,.10);overflow:hidden}
.abs{position:absolute}
.kicker{position:absolute;font-size:3.6px;color:var(--blue)}
.title{position:absolute;font-size:8.6px;color:var(--navy);font-weight:700;white-space:nowrap}
.title .hl{color:var(--blue)}
.center{left:0;width:100%;text-align:center}
.brand{position:absolute;display:flex;align-items:center;gap:2px;font-weight:700;color:var(--navy);font-size:7.5px;line-height:1}
.brand .dot{width:6px;height:6px;border-radius:50%;background:var(--navy)}
.page-num{position:absolute;left:262px;top:144px;font-size:4px;color:var(--ink)}
.page-num span{color:#c6c8cd;font-size:2.6px;margin-right:2px}
.photo{position:absolute}
.lorem{font-size:3px;line-height:1.5;color:var(--muted)}
.card{position:absolute;background:var(--card);box-shadow:var(--shadow);border-radius:2px}
.card.dark{background:var(--navy);color:#fff}
svg.icon{fill:none;stroke:var(--navy);stroke-width:1.2;stroke-linecap:round;stroke-linejoin:round}

/* cover */
.cover-title{position:absolute;left:25px;top:69px;font-size:12px;font-weight:700;color:var(--navy);letter-spacing:-.2px}
.cover-sub{position:absolute;left:27px;top:84px;font-size:4.6px;color:var(--blue)}
.cover-meta{position:absolute;left:25px;top:118px;font-size:5.6px;color:var(--navy);display:flex;gap:6px;align-items:center}
.cover-meta i{display:block;width:.6px;height:10px;background:var(--navy)}
.cover-web{position:absolute;left:238px;top:142px;font-size:4px;color:var(--ink)}

/* index */
.index-item{position:absolute;width:97px;display:flex;justify-content:space-between;font-size:3.6px;font-weight:700;color:var(--navy);border-bottom:.7px solid var(--rule);padding-bottom:1.5px}

/* bullets */
.section-head{position:absolute;font-size:4.4px;font-weight:700;color:var(--navy)}
.bullets{position:absolute;list-style:none;width:118px}
.bullets li{font-size:2.8px;line-height:1.5;color:var(--muted);padding-left:5px;position:relative;margin-bottom:3px}
.bullets li::before{content:"";position:absolute;left:1px;top:1.4px;width:1.3px;height:1.3px;border-radius:50%;background:var(--navy)}

.value-text{position:absolute;left:0;width:100%;text-align:center;font-size:3.6px;line-height:1.5;color:var(--muted)}
.card.dark .value-text{color:#fff}
.value-icon{position:absolute;left:32px;top:10px}

.feat-label{position:absolute;left:0;bottom:6px;width:100%;text-align:center;font-size:4px;font-weight:700;color:var(--navy)}
.feat-icon{position:absolute;left:14px;top:10px}

.band{position:absolute;left:0;top:41px;width:283px;height:62px;background:var(--navy)}
.fcard-head{position:absolute;left:7px;top:7px;display:flex;gap:4px;align-items:center;font-size:3.8px;font-weight:700;color:var(--navy)}
.card.dark .fcard-head{color:#fff}
.fcard-text{position:absolute;left:7px;top:19px;width:46px;font-size:3px;line-height:1.5;color:var(--muted)}
.card.dark .fcard-text{color:#dfe4f0}
.card.dark svg.icon{stroke:#fff}

/* right column */
.btn{position:absolute;left:29px;top:111px;width:44px;height:14px;border-radius:7px;background:var(--navy);color:#fff;font-size:3.8px;display:flex;align-items:center;padding-left:7px}
.btn b{position:absolute;right:3px;top:3px;width:8px;height:8px;border-radius:50%;border:.8px solid #fff}

.month{position:absolute;width:72px;text-align:center}
.month h4{font-size:5.4px;color:var(--navy);font-weight:700}
.month h4::after{content:"";display:block;width:6px;height:.6px;background:var(--blue);margin:1.5px auto 2px}
.month p{font-size:3px;line-height:1.5;color:var(--muted)}

.badge{position:absolute;width:50px;height:18px;background:#fafafa;border-radius:3px;box-shadow:var(--shadow);display:flex;align-items:center;justify-content:center}
.badge i{display:block;width:22px;height:5px;border-radius:3px;background:#d4d7de}

.step{position:absolute;top:45px;width:12px;height:12px;border-radius:50%;background:var(--navy);border:1.2px solid #c9d0e4;color:#fff;font-size:5px;display:flex;align-items:center;justify-content:center}
.tile{position:absolute;width:30px;height:29px;background:var(--card);box-shadow:var(--shadow)}
.tile span{position:absolute;bottom:3px;left:0;width:100%;text-align:center;font-size:3px;color:var(--ink)}
.tile svg{position:absolute;left:9px;top:6px}

.award-year{position:absolute;width:65px;text-align:center;font-size:5.2px;font-weight:700;color:var(--navy)}
.award-year::after{content:"";display:block;width:6px;height:.8px;background:var(--navy);margin:1.5px auto 0}
.award-text{position:absolute;width:65px;text-align:center;font-size:3px;line-height:1.55;color:var(--muted)}

.social{position:absolute;top:105px;width:9px;height:9px;border-radius:50%;border:.7px solid var(--navy)}
</style>
</head>
<body>

<!-- LEFT COLUMN -->
<section class="slide" style="left:71px;top:55px">
  <div class="photo" role="img" aria-label="Faint upward view of a glass office tower with soft abstract connected circles" style="left:100px;top:0;width:183px;height:157px;background:linear-gradient(160deg,rgba(242,242,242,0) 0%,#e2e3e5 45%,#d6d8db 100%)"></div>
  <div class="brand" style="left:25px;top:39px;font-size:15px;gap:4px"><span class="dot" style="width:11px;height:11px"></span>VeroTide</div>
  <h1 class="cover-title">PRESENTATION TITLE</h1>
  <p class="cover-sub">Business Presentation</p>
  <div class="cover-meta"><span>Mr. Evan Marlow</span><i></i><span>May&nbsp; 2023</span></div>
  <p class="cover-web">verotide.net</p>
</section>

<section class="slide" style="left:71px;top:230px">
  <p class="kicker" style="left:12px;top:10px">Business Presentation</p>
  <h2 class="title" style="left:12px;top:15px">Presentation <span class="hl">List</span></h2>
  <div class="index-item" style="left:32px;top:48px"><span>COVER SLIDES</span><span>01</span></div>
  <div class="index-item" style="left:32px;top:68px"><span>PRESENTATION LIST</span><span>02</span></div>
  <div class="index-item" style="left:32px;top:89px"><span>COMPANY OVERVIEW</span><span>03</span></div>
  <div class="index-item" style="left:32px;top:109px"><span>LOREM IPSUM PRESENTATION I</span><span>04</span></div>
  <div class="index-item" style="left:154px;top:48px"><span>TECHNOLOGY SUMMARY</span><span>05</span></div>
  <div class="index-item" style="left:154px;top:68px"><span>LOREM IPSUM PRESENTATION II</span><span>06</span></div>
  <div class="index-item" style="left:154px;top:89px"><span>LOREM IPSUM PRESENTATION III</span><span>07</span></div>
  <div class="index-item" style="left:154px;top:109px"><span>CLOSING SLIDE</span><span>08</span></div>
  <div class="brand" style="left:7px;top:143px"><span class="dot"></span>VeroTide</div>
  <p class="page-num"><span>page</span>5</p>
</section>

<section class="slide" style="left:71px;top:405px">
  <p class="kicker center" style="top:17px">Business Presentation</p>
  <h2 class="title center" style="top:22px">Presentation <span class="hl">List</span></h2>
  <div class="photo" role="img" aria-label="Twisting blue glass skyscraper against the sky" style="left:17px;top:45px;width:53px;height:65px;background:linear-gradient(160deg,#a9bdd6,#3c5a86 60%,#1b2a4a)"></div>
  <div class="photo" role="img" aria-label="Pale glass tower seen from below" style="left:76px;top:71px;width:52px;height:65px;background:linear-gradient(180deg,#fbfbfb,#e1e3e6 60%,#b9bdc4);box-shadow:var(--shadow)"></div>
  <h3 class="section-head" style="left:142px;top:45px">Section One</h3>
  <ul class="bullets" style="left:142px;top:52px">
    <li>Lorem ipsum dolor sit amet, consectetuer adipiscing elit. Maecenas porttitor congue massa. Fusce posuere, magna sed pulvinar ultricies.</li>
    <li>Lorem ipsum dolor sit amet, consectetuer adipiscing elit. Maecenas porttitor congue massa. Fusce posuere, magna sed pulvinar ultricies.</li>
    <li>Lorem ipsum dolor sit amet, consectetuer adipiscing elit. Maecenas porttitor congue massa. Fusce posuere, magna sed pulvinar ultricies.</li>
  </ul>
  <h3 class="section-head" style="left:144px;top:95px">Section Two</h3>
  <ul class="bullets" style="left:144px;top:102px">
    <li>Lorem ipsum dolor sit amet, consectetuer adipiscing elit. Maecenas porttitor congue massa. Fusce posuere, magna sed pulvinar ultricies.</li>
    <li>Lorem ipsum dolor sit amet, consectetuer adipiscing elit. Maecenas porttitor congue massa. Fusce posuere, magna sed pulvinar ultricies.</li>
    <li>Lorem ipsum dolor sit amet, consectetuer adipiscing elit. Maecenas porttitor congue massa. Fusce posuere, magna sed pulvinar ultricies.</li>
  </ul>
  <div class="brand" style="left:7px;top:143px"><span class="dot"></span>VeroTide</div>
  <p class="page-num"><span>page</span>7</p>
</section>

<section class="slide" style="left:71px;top:579px">
  <div class="brand" style="left:235px;top:8px"><span class="dot"></span>VeroTide</div>
  <p class="kicker center" style="top:17px">Business Presentation</p>
  <h2 class="title center" style="top:22px">Company Value</h2>
  <div class="card" style="left:55px;top:42px;width:73px;height:45px">
    <svg class="icon value-icon" width="8" height="8" viewBox="0 0 8 8"><circle cx="4" cy="3" r="1.8"/><path d="M1 7.5c.5-1.6 1.6-2.3 3-2.3s2.5.7 3 2.3"/></svg>
    <p class="value-text" style="top:24px">Global Company Services in<br>Lorem Vendor</p>
  </div>
  <div class="card dark" style="left:149px;top:42px;width:73px;height:45px">
    <svg class="icon value-icon" width="8" height="8" viewBox="0 0 8 8"><rect x="1" y="2" width="6" height="4" rx=".5"/><circle cx="6" cy="2" r="1"/></svg>
    <p class="value-text" style="top:23px">Best for Hardware Product<br>and Services</p>
  </div>
  <div class="card" style="left:55px;top:94px;width:73px;height:46px">
    <svg class="icon value-icon" width="8" height="8" viewBox="0 0 8 8"><path d="M2 1h3l1.5 1.5V7H2z"/><path d="M3 4h2.5M3 5.5h2"/></svg>
    <p class="value-text" style="top:24px">Than 15 Certifications<br>Company</p>
  </div>
  <div class="card" style="left:149px;top:94px;width:73px;height:46px">
    <svg class="icon value-icon" width="8" height="8" viewBox="0 0 8 8"><rect x=".8" y="1.5" width="5" height="3.6" rx=".4"/><circle cx="6" cy="4.5" r="1.1"/><path d="M4.6 7.5c.3-.9.8-1.3 1.4-1.3s1.1.4 1.4 1.3"/></svg>
    <p class="value-text" style="top:26px">Consulting and Full Support<br>Services</p>
  </div>
  <p class="page-num" style="top:143px"><span>page</span>9</p>
</section>

<section class="slide" style="left:71px;top:754px">
  <p class="kicker" style="left:12px;top:10px">Our Visions</p>
  <h2 class="title" style="left:12px;top:15px">Our Features</h2>
  <p class="lorem center" style="position:absolute;top:43px;font-size:3.8px;line-height:2.1">Lorem ipsum dolor sit amet, consectetuer adipiscing elit. Maecenas porttitor<br>congue massa. Fusce posuere, magna sed pulvinar ultricies.</p>
  <div class="card" style="left:20px;top:66px;width:52px;height:51px">
    <svg class="icon feat-icon" width="24" height="24" viewBox="0 0 24 24"><rect x="4" y="4" width="13" height="17" rx="1"/><path d="M8 3h5v3H8zM7 10l1 1 2-2M12 10h3M7 14l1 1 2-2M12 14h3M7 18h8"/><circle cx="19" cy="15" r="2.2"/></svg>
    <p class="feat-label">List Ipsum</p>
  </div>
  <div class="card" style="left:84px;top:66px;width:52px;height:51px">
    <svg class="icon feat-icon" width="24" height="24" viewBox="0 0 24 24"><path d="M6 14a4 4 0 0 1 .5-8 5 5 0 0 1 9.5 1 3.5 3.5 0 0 1 1 7z"/><circle cx="12" cy="10" r="2"/><path d="M8 14v5M12 14v6M16 14v5"/><circle cx="8" cy="20" r="1"/><circle cx="16" cy="20" r="1"/></svg>
    <p class="feat-label">Cloud Storage</p>
  </div>
  <div class="card" style="left:148px;top:66px;width:52px;height:51px">
    <svg class="icon feat-icon" width="24" height="24" viewBox="0 0 24 24"><path d="M3 6h7l2 2h9v12H3z"/><circle cx="13" cy="14" r="3"/><path d="M13 9.5v1.5M13 17v1.5M8.5 14H10M16 14h1.5"/></svg>
    <p class="feat-label">Data Monetization</p>
  </div>
  <div class="card" style="left:211px;top:66px;width:52px;height:51px">
    <svg class="icon feat-icon" width="24" height="24" viewBox="0 0 24 24"><circle cx="12" cy="12" r="3"/><circle cx="12" cy="3" r="1.5"/><circle cx="3" cy="18" r="1.5"/><circle cx="21" cy="18" r="1.5"/><circle cx="4" cy="8" r="1.2"/><circle cx="20" cy="8" r="1.2"/><path d="M12 4.5V9M4 17l5.5-3.5M20 17l-5.5-3.5M5 8.5l4.3 2.3M19 8.5l-4.3 2.3"/></svg>
    <p class="feat-label">Connectivity</p>
  </div>
  <div class="brand" style="left:7px;top:143px"><span class="dot"></span>VeroTide</div>
  <p class="page-num"><span>page</span>11</p>
</section>

<section class="slide" style="left:71px;top:929px">
  <p class="kicker" style="left:12px;top:10px">Our Visions</p>
  <h2 class="title" style="left:12px;top:15px">Our Features</h2>
  <div class="band" role="img" aria-label="Dark navy band with a faint circuit board texture"></div>
  <div class="card" style="left:13px;top:75px;width:60px;height:49px">
    <div class="fcard-head"><svg class="icon" width="8" height="8" viewBox="0 0 8 8"><rect x="1" y="1" width="6" height="4.5"/><path d="M3 7h2"/></svg>Mobile Montoring</div>
    <p class="fcard-text">Lorem ipsum dolor sit amet, consectetuer adipiscing elit. Maecenas porttitor congue massa. Fusce posuere</p>
  </div>
  <div class="card dark" style="left:78px;top:75px;width:61px;height:49px">
    <div class="fcard-head"><svg class="icon" width="8" height="8" viewBox="0 0 8 8"><rect x="1" y="1" width="6" height="4.5"/><circle cx="4" cy="3.2" r="1"/></svg>Secure Sysems</div>
    <p class="fcard-text">Lorem ipsum dolor sit amet, consectetuer adipiscing elit. Maecenas porttitor congue massa. Fusce posuere</p>
  </div>
  <div class="card" style="left:144px;top:75px;width:60px;height:49px">
    <div class="fcard-head"><svg class="icon" width="8" height="8" viewBox="0 0 8 8"><rect x="1" y="1" width="6" height="6"/><path d="M2.5 6V4.5M4 6V3M5.5 6V4"/></svg>Analytics</div>
    <p class="fcard-text">Lorem ipsum dolor sit amet, consectetuer adipiscing elit. Maecenas porttitor congue massa. Fusce posuere</p>
  </div>
  <div class="card" style="left:209px;top:75px;width:61px;height:49px">
    <div class="fcard-head"><svg class="icon" width="8" height="8" viewBox="0 0 8 8"><rect x="1" y="1" width="6" height="4.5"/><path d="M3 7h2M4 5.5V7"/></svg>Saving Money</div>
    <p class="fcard-text">Lorem ipsum dolor sit amet, consectetuer adipiscing elit. Maecenas porttitor congue massa. Fusce posuere</p>
  </div>
  <div class="brand" style="left:7px;top:143px"><span class="dot"></span>VeroTide</div>
  <p class="page-num"><span>page</span>13</p>
</section>

<!-- RIGHT COLUMN -->
<section class="slide" style="left:372px;top:90px">
  <p class="kicker" style="left:30px;top:32px">Presentation&nbsp; Slides</p>
  <h2 class="title" style="left:30px;top:37px">Our Slides</h2>
  <p class="lorem" style="position:absolute;left:30px;top:55px;width:118px;font-size:3.2px;line-height:1.9"><b style="color:var(--ink)">Lorem ipsum dolor sit amet</b>, consectetuer adipiscing elit. Maecenas porttitor congue massa. Fusce posuere, magna sed pulvinar ultricies, purus lectus malesuada libero, sit amet comeuin commodo magna eros quis urna. Nunec viverra imperdiet enim.</p>
  <div class="btn">More Info<b></b></div>
  <div class="photo" role="img" aria-label="Laptop, coffee cup and notebook on a desk by a wooden wall" style="left:179px;top:31px;width:74px;height:95px;background:linear-gradient(180deg,#6b4a35 0%,#8a6a52 45%,#c9c4be 70%,#e8e6e3 100%)"></div>
  <div class="brand" style="left:7px;top:143px"><span class="dot"></span>VeroTide</div>
  <p class="page-num"><span>page</span>6</p>
</section>

<section class="slide" style="left:372px;top:264px">
  <p class="kicker center" style="top:17px">Business Presentation</p>
  <h2 class="title center" style="top:22px">Presentation <span class="hl">List</span></h2>
  <div class="abs" style="left:105px;top:41px;width:73px;height:45px;border:.6px solid #c5cad6;border-radius:2px;background:rgba(255,255,255,.35)"></div>
  <div class="month" style="left:17px;top:50px"><h4>June</h4><p>Lorem ipsum dolor sit amet, consecter adipiscing eli Maecenas porttitor adipiscing elit tam emotan.</p></div>
  <div class="month" style="left:105px;top:50px"><h4>July</h4><p>Lorem ipsum dolor sit amet, consecter adipiscing eli Maecenas porttitor adipiscing elit tam emotan.</p></div>
  <div class="month" style="left:193px;top:50px"><h4>August</h4><p>Lorem ipsum dolor sit amet, consecter adipiscing eli Maecenas porttitor adipiscing elit tam emotan.</p></div>
  <div class="month" style="left:17px;top:105px"><h4>September</h4><p>Lorem ipsum dolor sit amet, consecter adipiscing eli Maecenas porttitor adipiscing elit tam emotan.</p></div>
  <div class="month" style="left:105px;top:105px"><h4>October</h4><p>Lorem ipsum dolor sit amet, consecter adipiscing eli Maecenas porttitor adipiscing elit tam emotan.</p></div>
  <div class="month" style="left:193px;top:105px"><h4>November</h4><p>Lorem ipsum dolor sit amet, consecter adipiscing eli Maecenas porttitor adipiscing elit tam emotan.</p></div>
  <div class="brand" style="left:7px;top:143px"><span class="dot"></span>VeroTide</div>
  <p class="page-num"><span>page</span>8</p>
</section>

<section class="slide" style="left:372px;top:439px">
  <p class="kicker center" style="top:17px">Business Partner</p>
  <h2 class="title center" style="top:22px">Our Partnership</h2>
  <div class="badge" style="left:29px;top:60px"><i></i></div>
  <div class="badge" style="left:87px;top:60px"><i></i></div>
  <div class="badge" style="left:145px;top:60px"><i></i></div>
  <div class="badge" style="left:203px;top:60px"><i></i></div>
  <div class="badge" style="left:29px;top:88px"><i></i></div>
  <div class="badge" style="left:87px;top:88px"><i></i></div>
  <div class="badge" style="left:145px;top:88px"><i></i></div>
  <div class="badge" style="left:203px;top:88px"><i></i></div>
  <div class="brand" style="left:7px;top:143px"><span class="dot"></span>VeroTide</div>
  <p class="page-num"><span>page</span>10</p>
</section>

<section class="slide" style="left:372px;top:614px">
  <p class="kicker" style="left:12px;top:10px">Our Visions</p>
  <h2 class="title" style="left:12px;top:15px">Timeline</h2>
  <div class="abs" style="left:41px;top:51px;width:198px;border-top:.6px dashed var(--navy)"></div>
  <div class="step" style="left:35px">1</div>
  <div class="step" style="left:132px">2</div>
  <div class="step" style="left:233px">3</div>
  <div class="card" style="left:16px;top:73px;width:51px;height:41px;border-radius:0"><span class="abs" style="left:21px;top:16px;width:9px;height:9px;border-radius:50%;background:var(--navy)"></span></div>
  <div class="tile" style="left:89px;top:65px"><svg class="icon" width="12" height="12" viewBox="0 0 12 12"><path d="M6 1.5c-2.5 0-4 1.6-4 3.8 0 1.5.7 2.3 1.5 3V10h5V8.3c.8-.7 1.5-1.5 1.5-3 0-2.2-1.5-3.8-4-3.8zM6 1.5V10"/></svg><span>Biotech</span></div>
  <div class="tile" style="left:125px;top:65px"><svg class="icon" width="12" height="12" viewBox="0 0 12 12"><path d="M3.5 1.5h5v3a2.5 2.5 0 0 1-5 0zM6 7v2.5M4 10.5h4"/></svg><span>Sports</span></div>
  <div class="tile" style="left:161px;top:65px"><svg class="icon" width="12" height="12" viewBox="0 0 12 12"><rect x="3.5" y="3.5" width="5" height="5"/><path d="M6 1v2.5M6 8.5V11M1 6h2.5M8.5 6H11"/></svg><span>Fintech</span></div>
  <div class="tile" style="left:89px;top:98px"><svg class="icon" width="12" height="12" viewBox="0 0 12 12"><path d="M2 11V4l4-2.5L10 4v7zM4.5 6h1M6.5 6h1M4.5 8h1M6.5 8h1"/></svg><span>Real State</span></div>
  <div class="tile" style="left:125px;top:98px"><svg class="icon" width="12" height="12" viewBox="0 0 12 12"><rect x="2" y="1.5" width="7" height="9"/><path d="M3.5 4h4M3.5 6h4M3.5 8h2.5"/></svg><span>Commodities</span></div>
  <div class="tile" style="left:161px;top:98px"><svg class="icon" width="12" height="12" viewBox="0 0 12 12"><circle cx="2" cy="2" r=".8"/><circle cx="6" cy="2" r=".8"/><circle cx="10" cy="2" r=".8"/><circle cx="2" cy="6" r=".8"/><circle cx="10" cy="6" r=".8"/><circle cx="2" cy="10" r=".8"/><circle cx="6" cy="10" r=".8"/><circle cx="10" cy="10" r=".8"/><path d="M2.8 2.8l2.4 2.4M9.2 2.8L6.8 5.2"/></svg><span>ESG</span></div>
  <div class="card" style="left:214px;top:73px;width:51px;height:41px;border-radius:0;display:flex;align-items:center;justify-content:center;font-size:6px;color:var(--navy)">Result</div>
</section>

<section class="slide" style="left:372px;top:789px">
  <p class="kicker center" style="top:17px">Business Partner</p>
  <h2 class="title center" style="top:22px">Our Partnership</h2>
  <div class="photo" role="img" aria-label="Glass award trophy on a dark background" style="left:19px;top:47px;width:65px;height:40px;background:linear-gradient(135deg,#141414,#3a3d42 55%,#1a1a1a)"></div>
  <div class="photo" role="img" aria-label="Gold trophy cup on a light grey background" style="left:108px;top:47px;width:65px;height:40px;background:linear-gradient(180deg,#d9d9d9,#c7c4bd 60%,#b0aca4)"></div>
  <div class="photo" role="img" aria-label="Hand holding a glass sphere against a dark background" style="left:198px;top:47px;width:65px;height:40px;background:radial-gradient(circle at 45% 55%,#8a4a2c 0%,#3a2217 30%,#111 70%)"></div>
  <p class="award-year" style="left:19px;top:95px">2019</p>
  <p class="award-year" style="left:108px;top:95px">2020</p>
  <p class="award-year" style="left:198px;top:94px">2021</p>
  <p class="award-text" style="left:19px;top:108px">Lorem ipsum dolor sit amet, consectetuer adipisc. Maecenas porttitor congue massa kame.</p>
  <p class="award-text" style="left:108px;top:108px">Lorem ipsum dolor sit amet, consectetuer adipisc. Maecenas porttitor congue massa kame.</p>
  <p class="award-text" style="left:198px;top:107px">Lorem ipsum dolor sit amet, consectetuer adipisc. Maecenas porttitor congue massa kame.</p>
  <div class="brand" style="left:7px;top:143px"><span class="dot"></span>VeroTide</div>
  <p class="page-num"><span>page</span>14</p>
</section>

<section class="slide" style="left:372px;top:964px">
  <h2 class="title center" style="top:52px;font-size:17px;font-weight:900">Thank You</h2>
  <div class="abs" style="left:82px;top:76px;width:119px;height:.7px;background:var(--navy)"></div>
  <p class="center abs" style="top:81px;font-size:3.3px;line-height:1.8;color:var(--ink)">Lorem ipsum dolor sit amet, consectetuer adipiscing elit. Maecen portion congue<br>massa. Fusce posuere, magna sed pulvinar ultricies, purus lectus.</p>
  <span class="social" style="left:115px"></span>
  <span class="social" style="left:137px"></span>
  <span class="social" style="left:160px"></span>
</section>

</body>
</html>
```